IT Company based on Biology Business Needs a PowerPoint Design

We need a powerpoint design for a new company called 'Tall FERN'. We develop the machine learning solutions especially focused on deep learning algorithms for biology industry. Our initial product is a vision detection on biological images to help doctors diagnose the symptoms. We would like to see designs that use the color green.

Industry/Entity Type

Biotechnology

Requirements
Nice to have
• Lots of slide templates with company logo's look and feel

```html
<!DOCTYPE html>
<html lang="en">
<head>
<meta charset="utf-8">
<title>Tall FERN – Presentation Templates</title>
<link rel="stylesheet" href="https://fonts.googleapis.com/css2?family=Open+Sans:wght@400;600&display=swap">
<style>
  :root {
    --page-bg: #e9ecef;
    --slide-bg: #fafafa;
    --fern-light: #55b531;
    --fern-dark: #0b7a33;
    --fern-text: #3aa635;
    --deco-tint: #eceeed;
    --bullet-text: #3b3b3b;
    --white: #ffffff;
  }
  * { box-sizing: border-box; margin: 0; padding: 0; }
  html, body { width: 1200px; height: 800px; overflow: hidden; }
  body {
    background: var(--page-bg);
    font-family: "Open Sans", Arial, sans-serif;
    position: relative;
  }
  .slide {
    position: absolute;
    width: 480px;
    height: 360px;
    background: var(--slide-bg);
    overflow: hidden;
    box-shadow: 0 3px 10px rgba(0,0,0,.18);
  }
  .slide--title   { left: 100px; top: 20px; }
  .slide--content { left: 620px; top: 20px; }
  .slide--closing { left: 360px; top: 420px; }

  .slide__curve { position: absolute; inset: 0; width: 100%; height: 100%; }

  .slide__deco {
    position: absolute;
    right: 0;
    background: linear-gradient(200deg, rgba(236,238,237,0) 0%, rgba(225,229,227,.55) 60%, rgba(225,229,227,0) 100%);
  }
  .slide--title .slide__deco,
  .slide--closing .slide__deco { top: 150px; width: 170px; height: 210px; background: linear-gradient(200deg, rgba(255,255,255,0) 0%, rgba(255,255,255,.12) 55%, rgba(255,255,255,0) 100%); }
  .slide--content .slide__deco { top: 140px; width: 180px; height: 190px; }

  .brand {
    position: absolute;
    display: flex;
    align-items: center;
    gap: 6px;
    color: var(--fern-text);
    font-weight: 400;
    font-size: 19px;
    letter-spacing: .5px;
    white-space: nowrap;
  }
  .brand__dot {
    width: 11px; height: 11px;
    border-radius: 50%;
    background: var(--fern-light);
  }
  .slide--title .brand,
  .slide--closing .brand { left: 50%; top: 64px; transform: translateX(-50%); }
  .slide--content .brand { right: 34px; top: 58px; }

  .slide__welcome {
    position: absolute;
    left: 0; right: 0; top: 240px;
    text-align: center;
    color: var(--white);
    font-size: 26px;
    font-weight: 400;
  }

  .slide__heading {
    position: absolute;
    left: 38px; top: 64px;
    color: var(--fern-text);
    font-size: 17px;
    font-weight: 400;
  }
  .point-list {
    position: absolute;
    left: 72px; top: 118px;
    list-style: none;
    color: var(--bullet-text);
    font-size: 12.5px;
    line-height: 15.5px;
  }
  .point-list li::before { content: "»"; margin-right: 8px; }
  .slide__footer-band {
    position: absolute;
    left: 0; right: 0; bottom: 0;
    height: 25px;
    background: var(--fern-dark);
  }

  .contact {
    position: absolute;
    left: 0; right: 0; top: 248px;
    text-align: center;
    color: var(--white);
    font-size: 7.5px;
    line-height: 14px;
  }
  .contact__line { display: flex; justify-content: center; align-items: center; gap: 4px; }
  .contact__icon { width: 8px; height: 8px; fill: var(--white); }
  .contact__gap { width: 8px; }
</style>
</head>
<body>

<section class="slide slide--title" aria-label="Title slide">
  <svg class="slide__curve" viewBox="0 0 480 360" preserveAspectRatio="none" aria-hidden="true">
    <path d="M0 200 Q240 110 480 196 L480 360 L0 360 Z" fill="var(--fern-dark)"/>
    <path d="M0 206 Q240 124 480 202 L480 360 L0 360 Z" fill="var(--fern-light)"/>
  </svg>
  <div class="slide__deco" role="img" aria-label="Faint brand-symbol decoration"></div>
  <div class="brand"><span class="brand__dot"></span>TALL FERN</div>
  <h1 class="slide__welcome">Welcome</h1>
</section>

<section class="slide slide--content" aria-label="Content slide">
  <div class="slide__deco" role="img" aria-label="Faint brand-symbol decoration"></div>
  <div class="brand"><span class="brand__dot"></span>TALL FERN</div>
  <h2 class="slide__heading">Body Text</h2>
  <ul class="point-list">
    <li>point no. 1</li>
    <li>point no. 1</li>
    <li>point no. 1</li>
    <li>point no. 1</li>
    <li>point no. 1</li>
  </ul>
  <div class="slide__footer-band"></div>
</section>

<section class="slide slide--closing" aria-label="Closing slide">
  <svg class="slide__curve" viewBox="0 0 480 360" preserveAspectRatio="none" aria-hidden="true">
    <path d="M0 200 Q240 110 480 196 L480 360 L0 360 Z" fill="var(--fern-dark)"/>
    <path d="M0 206 Q240 124 480 202 L480 360 L0 360 Z" fill="var(--fern-light)"/>
  </svg>
  <div class="slide__deco" role="img" aria-label="Faint brand-symbol decoration"></div>
  <div class="brand"><span class="brand__dot"></span>TALL FERN</div>
  <address class="contact">
    <div class="contact__line">Your Long Commercial or business address in 2 line</div>
    <div class="contact__line">
      <svg class="contact__icon" viewBox="0 0 10 10" aria-hidden="true"><path d="M2 1h2l1 2.5-1.3 1a5 5 0 0 0 1.8 1.8l1-1.3L9 6v2a1 1 0 0 1-1 1A7 7 0 0 1 1 2a1 1 0 0 1 1-1z"/></svg>
      +00 123 456 7890
    </div>
    <div class="contact__line">
      <svg class="contact__icon" viewBox="0 0 10 10" aria-hidden="true"><path d="M0 2h10v6H0z M0 2l5 3.5L10 2" fill="none" stroke="#fff" stroke-width="1"/></svg>
      hello@tallfern.bio
      <span class="contact__gap"></span>
      <svg class="contact__icon" viewBox="0 0 10 10" aria-hidden="true"><circle cx="5" cy="5" r="4.3" fill="none" stroke="#fff" stroke-width="1"/><path d="M.7 5h8.6M5 .7c-2.5 2.8-2.5 5.8 0 8.6M5 .7c2.5 2.8 2.5 5.8 0 8.6" fill="none" stroke="#fff" stroke-width=".8"/></svg>
      www.tallfern.bio
    </div>
  </address>
</section>

</body>
</html>
```